Brenwick Drilling Inc. Business card design

Business card design for "Brenwick Drilling Inc. - Directional Drilling Services"

Address is:

Brenwick Drilling Inc.
512 - 73 Tolvane Crescent SW
Calgary, Alberta, Canada
T2K 4P8

Please incorporate the logo design into the card, thank you.

Target Market(s)

Oil & Gas and Drilling

Industry/Entity Type

Business

```html
<!DOCTYPE html>
<html lang="en">
<head>
<meta charset="utf-8">
<title>Brenwick Drilling Inc. – Business Card</title>
<link href="https://fonts.googleapis.com/css2?family=Montserrat:wght@500;800&family=Open+Sans:wght@400&display=swap" rel="stylesheet">
<style>
  :root {
    --backdrop: #c8c8c8;
    --card-black: #0d0d0f;
    --card-white: #f6f6f6;
    --ink: #111111;
    --accent-red: #d2381f;
    --soft-grey: #d9d9d9;
  }
  * { box-sizing: border-box; margin: 0; padding: 0; }
  html, body { width: 1200px; height: 1001px; overflow: hidden; }
  body {
    background: var(--backdrop);
    position: relative;
    font-family: "Open Sans", sans-serif;
  }
  .card {
    position: absolute;
    top: 352px;
    width: 520px;
    height: 297px;
    overflow: hidden;
  }
  .card--front { left: 40px; background: var(--card-black); }
  .card--back { left: 640px; background: var(--card-white); }

  .front-brand {
    position: absolute; inset: 0;
    display: flex; flex-direction: column; align-items: center; justify-content: center; gap: 18px;
  }
  .brand-dot {
    width: 46px; height: 46px; border-radius: 50%;
    border: 4px solid var(--accent-red);
  }
  .brand-name {
    font-family: "Montserrat", sans-serif;
    font-weight: 800;
    text-transform: uppercase;
    letter-spacing: 0.02em;
  }
  .front-brand .brand-name { color: var(--card-white); font-size: 22px; }

  .back-top {
    position: absolute; left: 0; top: 0; width: 100%; height: 165px;
    display: flex; align-items: center; gap: 18px; padding-left: 34px;
  }
  .back-top .brand-dot { width: 56px; height: 56px; flex: none; }
  .back-top .brand-name { color: var(--ink); font-size: 27px; line-height: 1; }
  .tagline {
    font-family: "Montserrat", sans-serif;
    font-weight: 500;
    font-size: 11.5px;
    letter-spacing: 0.22em;
    text-transform: uppercase;
    color: var(--ink);
    margin-top: 6px;
  }
  .back-band {
    position: absolute; left: 0; bottom: 0; width: 100%; height: 132px;
    background: var(--card-black);
  }
  .address {
    position: absolute; left: 255px; top: 22px;
    font-style: normal; font-size: 14px; line-height: 1.45;
    color: var(--soft-grey);
  }
  .address .company { color: var(--accent-red); }
</style>
</head>
<body>
  <section class="card card--front" aria-label="Card front">
    <div class="front-brand">
      <span class="brand-dot"></span>
      <span class="brand-name">Brenwick Drilling Inc.</span>
    </div>
  </section>

  <section class="card card--back" aria-label="Card back">
    <div class="back-top">
      <span class="brand-dot"></span>
      <div>
        <div class="brand-name">Brenwick Drilling Inc.</div>
        <div class="tagline">Directional Drilling Services</div>
      </div>
    </div>
    <div class="back-band">
      <address class="address">
        <span class="company">Brenwick Drilling Inc.</span><br>
        512 - 73 Tolvane Crescent SW<br>
        Calgary, Alberta, Canada<br>
        T2K 4P8
      </address>
    </div>
  </section>
</body>
</html>
```